Branding Pack for new business to business cost saving site

I would like a branding pack for my new project. I would like the following designed;
a4 Presentation folder
Letterhead
Envelope
Business Card
compliment splip

We are a business cost saving site, we have access to 1000s of discount offers for daily business to business offers. I already have the logo therfore please follow th e logo for the coloutr and design.

Target Market(s)

SMEs in United Kingdom

Industry/Entity Type

Business Service

Font styles to use
Serif
Script

Colors
0255a3
fbee3d

Requirements
Must have
• The folder needs to be the same size as attached

```html
<!DOCTYPE html>
<html lang="en">
<head>
<meta charset="utf-8">
<title>tallymate – Folder and Compliment Slip</title>
<link href="https://fonts.googleapis.com/css2?family=Comfortaa:wght@500&family=Montserrat:wght@400;600&family=Pinyon+Script&display=swap" rel="stylesheet">
<style>
  :root {
    --navy: #2e3677;
    --navy-deep: #293170;
    --yellow: #fed448;
    --paper: #ffffff;
    --stage: #cfcfcf;
    --ghost: #ececec;
    --muted: #b9bde0;
  }
  * { margin: 0; padding: 0; box-sizing: border-box; }
  html, body {
    width: 1200px; height: 954px; overflow: hidden;
    background: var(--stage);
    font-family: "Montserrat", sans-serif;
  }
  .canvas { position: relative; width: 1200px; height: 954px; }

  /* Presentation folder spread */
  .folder {
    position: absolute; left: 70px; top: 40px;
    width: 760px; height: 537px;
    display: flex; overflow: hidden;
    background: var(--navy);
  }
  .folder-panel { position: relative; width: 380px; height: 537px; }
  .folder-back { background: var(--navy-deep); }
  .folder-front { border-left: 1px solid rgba(0,0,0,0.12); }
  .folder-circle {
    position: absolute; left: 250px; top: 45px;
    width: 260px; height: 260px; border-radius: 50%;
    background: var(--yellow);
  }
  .wordmark {
    font-family: "Comfortaa", sans-serif; font-weight: 500;
    letter-spacing: 0.5px; line-height: 1;
    display: flex; align-items: center; gap: 6px;
  }
  .wordmark-dot { width: 9px; height: 9px; border-radius: 50%; background: var(--yellow); }
  .tagline {
    font-size: 5px; letter-spacing: 2.4px; text-transform: uppercase;
    margin-top: 4px; white-space: nowrap;
  }
  .back-brand {
    position: absolute; left: 0; right: 0; bottom: 70px;
    text-align: center; color: #fff;
  }
  .back-brand .wordmark { justify-content: center; font-size: 22px; }
  .back-brand .tagline { color: var(--muted); }
  .back-contact { font-size: 6.5px; color: var(--muted); line-height: 1.6; margin-top: 10px; }
  .back-contact b { color: #fff; font-weight: 600; }
  .front-brand {
    position: absolute; right: 36px; bottom: 58px; color: #fff; text-align: center;
  }
  .front-brand .wordmark { font-size: 32px; }
  .front-brand .tagline { color: var(--muted); font-size: 6px; }

  /* Compliment slip */
  .slip {
    position: absolute; left: 640px; top: 660px;
    width: 490px; height: 231px;
    background: var(--paper); overflow: hidden;
  }
  .slip-ghost {
    position: absolute; left: 290px; top: 30px;
    width: 150px; height: 150px; border-radius: 50%;
    background: var(--ghost);
  }
  .slip-brand { position: absolute; left: 36px; top: 34px; color: var(--navy); }
  .slip-brand .wordmark { font-size: 26px; }
  .slip-brand .tagline { color: #8a8fb8; font-size: 4.5px; }
  .slip-contact {
    position: absolute; left: 36px; bottom: 20px;
    font-size: 6px; color: var(--navy); line-height: 1.6;
  }
  .slip-contact b { font-weight: 600; }
  .slip-greeting {
    position: absolute; right: 34px; bottom: 18px;
    font-family: "Pinyon Script", cursive; font-size: 19px; color: var(--navy);
  }
</style>
</head>
<body>
<main class="canvas">
  <section class="folder" aria-label="A4 presentation folder, outer spread">
    <div class="folder-panel folder-back">
      <div class="back-brand">
        <div class="wordmark">tallymate<span class="wordmark-dot"></span></div>
        <div class="tagline">Spend smarter every single day</div>
        <p class="back-contact">Suite 2, 14 Harbour Lane, Brightwater QLD 4820<br>
          <b>T:</b> +61 7 4000 1234 · <b>E:</b> hello@tallymate.com · www.<b>tallymate</b>.com</p>
      </div>
    </div>
    <div class="folder-panel folder-front">
      <div class="front-brand">
        <div class="wordmark">tallymate<span class="wordmark-dot"></span></div>
        <div class="tagline">Spend smarter every single day</div>
      </div>
    </div>
    <div class="folder-circle"></div>
  </section>

  <section class="slip" aria-label="Compliment slip">
    <div class="slip-ghost"></div>
    <div class="slip-brand">
      <div class="wordmark">tallymate<span class="wordmark-dot"></span></div>
      <div class="tagline">Spend smarter every single day</div>
    </div>
    <p class="slip-contact">Suite 2, 14 Harbour Lane, Brightwater QLD 4820<br>
      <b>T:</b> +61 7 4000 1234 · <b>E:</b> hello@tallymate.com · www.<b>tallymate</b>.com</p>
    <p class="slip-greeting">With Compliments</p>
  </section>
</main>
</body>
</html>
```